Security Guard Company Postcard

I am looking for a postcard to be created so I can send to potential clients for sales and marketing purposes for my security guard division. NOT Investigations! I have added a photo of my logo and I am looking to have the following services included:
Permanent Security Services
Temporary Security Services
Emergency Services
Fire Watch
Alarm Response
Private Investigations
Background Checks
ALPR Camera Systems

Are just to name a few of our services. Please contact me at mdunbar@pivanco.com for any questions.
Thank you!
Marcus

Security

Security

• Any wording on Investigations

```html
<!DOCTYPE html>
<html lang="en">
<head>
<meta charset="utf-8">
<title>Kestrel Security Postcard</title>
<link rel="stylesheet" href="https://fonts.googleapis.com/css2?family=Montserrat:ital,wght@0,500;0,600;0,700;0,800;1,600;1,700;1,800&family=Open+Sans:wght@400;600&display=swap">
<style>
:root{
  --navy:#1b2350;
  --navy-deep:#141a3d;
  --blue:#1a66b8;
  --sky:#2a9ad6;
  --cyan:#3fc1ea;
  --white:#ffffff;
  --stage:#eceef1;
  --photo-a:#5d6570;
  --photo-b:#c9ced4;
}
*{box-sizing:border-box;margin:0;padding:0}
html,body{width:876px;height:1200px;overflow:hidden}
body{background:var(--stage);font-family:"Open Sans",Arial,sans-serif;position:relative}
.card{position:absolute;left:40px;width:796px;background:var(--white);overflow:hidden}
.front{top:30px;height:560px}
.back{top:620px;height:540px}

/* brand */
.brand{display:flex;align-items:center;gap:10px;font-family:"Montserrat",Arial,sans-serif;font-weight:800;color:var(--navy);letter-spacing:1px}
.brand-dot{width:34px;height:34px;border-radius:50%;background:var(--navy)}

/* front */
.front .brand{position:absolute;left:28px;top:14px;font-size:36px}
.headline{position:absolute;right:0;top:0;width:470px;height:62px;background:linear-gradient(90deg,var(--blue),var(--sky));clip-path:polygon(6% 0,100% 0,100% 100%,0 100%);display:flex;flex-direction:column;justify-content:center;padding-left:48px;color:var(--white);font-family:"Montserrat",sans-serif;font-style:italic}
.headline .small{font-size:17px;font-weight:700;letter-spacing:.3px}
.headline .big{font-size:25px;font-weight:800;line-height:1.05}
.photo{position:absolute;right:0;top:62px;width:520px;height:418px;background:linear-gradient(135deg,var(--photo-b),var(--photo-a))}
.services{position:absolute;left:0;top:74px;width:345px;height:406px;background:var(--navy);clip-path:polygon(0 0,100% 0,82% 100%,0 100%);padding:28px 0 0 32px;color:var(--white)}
.services h2{font-family:"Montserrat",sans-serif;font-style:italic;font-weight:800;font-size:22px;margin-bottom:6px}
.services .rule{width:180px;height:3px;background:var(--cyan);margin-bottom:18px}
.services ul{list-style:none}
.services li{display:flex;align-items:center;gap:10px;font-family:"Montserrat",sans-serif;font-style:italic;font-weight:600;font-size:16px;margin-bottom:12px}
.shield{width:18px;height:20px;flex:none}
.footer{position:absolute;left:0;bottom:0;width:100%;height:80px;background:var(--navy-deep);display:flex;align-items:center;color:var(--white)}
.call{height:100%;width:255px;background:var(--sky);clip-path:polygon(0 0,100% 0,90% 100%,0 100%);padding:14px 0 0 26px;font-family:"Montserrat",sans-serif}
.call .label{font-size:12px;font-weight:600;letter-spacing:1px}
.call .num{display:flex;align-items:center;gap:8px;font-size:24px;font-weight:800}
.contact{display:flex;align-items:flex-start;gap:8px;font-size:13px;line-height:1.35;padding-left:24px}
.contact.addr{width:270px}
.contact svg{flex:none;margin-top:2px}

/* back */
.promo{position:absolute;left:0;top:0;width:290px;height:430px;background:var(--navy);padding:36px 0 0 30px;color:var(--white)}
.promo h2{font-family:"Montserrat",sans-serif;font-weight:800;font-size:22px;line-height:1.2}
.promo .rule{width:170px;height:3px;background:var(--cyan);margin:12px 0 18px}
.promo p{font-size:14px;line-height:1.45;color:#cfd6ee;width:220px;margin-bottom:22px}
.feature{display:flex;align-items:center;gap:12px;font-family:"Montserrat",sans-serif;font-style:italic;font-weight:700;font-size:15px;line-height:1.2;margin-bottom:18px}
.feature .shield{width:28px;height:32px}
.web{display:flex;align-items:center;gap:8px;font-size:13px;margin-top:18px}
.back-call{position:absolute;left:0;top:430px;width:290px;height:40px;background:var(--sky);display:flex;align-items:center;gap:10px;padding-left:30px;color:var(--white);font-family:"Montserrat",sans-serif}
.back-call .label{font-size:12px;font-weight:600;letter-spacing:1px}
.back-call .num{font-size:20px;font-weight:800}
.back .brand{position:absolute;left:30px;top:482px;font-size:38px}
</style>
</head>
<body>

<section class="card front">
  <div class="brand"><span class="brand-dot"></span>KESTREL</div>

  <div class="headline">
    <span class="small">STAY SECURE WITH OUR RELIABLE</span>
    <span class="big">SECURITY GUARD SERVICES</span>
  </div>

  <div class="photo" role="img" aria-label="Photo of a security guard in a black uniform and cap speaking into a handheld radio"></div>

  <div class="services">
    <h2>OUR SERVICES</h2>
    <div class="rule"></div>
    <ul>
      <li><svg class="shield" viewBox="0 0 18 20"><path d="M9 0L18 3v6c0 6-4 9-9 11C4 18 0 15 0 9V3z" fill="#3fc1ea"/><path d="M5 10l3 3 5-6" stroke="#1b2350" stroke-width="2" fill="none"/></svg>Permanent Security Services</li>
      <li><svg class="shield" viewBox="0 0 18 20"><path d="M9 0L18 3v6c0 6-4 9-9 11C4 18 0 15 0 9V3z" fill="#3fc1ea"/><path d="M5 10l3 3 5-6" stroke="#1b2350" stroke-width="2" fill="none"/></svg>Temporary Security Services</li>
      <li><svg class="shield" viewBox="0 0 18 20"><path d="M9 0L18 3v6c0 6-4 9-9 11C4 18 0 15 0 9V3z" fill="#3fc1ea"/><path d="M5 10l3 3 5-6" stroke="#1b2350" stroke-width="2" fill="none"/></svg>Emergency Services</li>
      <li><svg class="shield" viewBox="0 0 18 20"><path d="M9 0L18 3v6c0 6-4 9-9 11C4 18 0 15 0 9V3z" fill="#3fc1ea"/><path d="M5 10l3 3 5-6" stroke="#1b2350" stroke-width="2" fill="none"/></svg>Fire Watch</li>
      <li><svg class="shield" viewBox="0 0 18 20"><path d="M9 0L18 3v6c0 6-4 9-9 11C4 18 0 15 0 9V3z" fill="#3fc1ea"/><path d="M5 10l3 3 5-6" stroke="#1b2350" stroke-width="2" fill="none"/></svg>Alarm Response</li>
      <li><svg class="shield" viewBox="0 0 18 20"><path d="M9 0L18 3v6c0 6-4 9-9 11C4 18 0 15 0 9V3z" fill="#3fc1ea"/><path d="M5 10l3 3 5-6" stroke="#1b2350" stroke-width="2" fill="none"/></svg>Private Investigations</li>
      <li><svg class="shield" viewBox="0 0 18 20"><path d="M9 0L18 3v6c0 6-4 9-9 11C4 18 0 15 0 9V3z" fill="#3fc1ea"/><path d="M5 10l3 3 5-6" stroke="#1b2350" stroke-width="2" fill="none"/></svg>Background Checks</li>
      <li><svg class="shield" viewBox="0 0 18 20"><path d="M9 0L18 3v6c0 6-4 9-9 11C4 18 0 15 0 9V3z" fill="#3fc1ea"/><path d="M5 10l3 3 5-6" stroke="#1b2350" stroke-width="2" fill="none"/></svg>ALPR Camera Systems</li>
    </ul>
  </div>

  <div class="footer">
    <div class="call">
      <div class="label">CALL US NOW</div>
      <div class="num"><svg width="20" height="20" viewBox="0 0 24 24"><path d="M6.6 10.8a15 15 0 006.6 6.6l2.2-2.2c.3-.3.7-.4 1-.2 1.1.4 2.3.6 3.6.6.6 0 1 .4 1 1V20c0 .6-.4 1-1 1A17 17 0 013 4c0-.6.4-1 1-1h3.5c.6 0 1 .4 1 1 0 1.3.2 2.5.6 3.6.1.3 0 .7-.2 1z" fill="#fff"/></svg>555-014-2290</div>
    </div>
    <div class="contact addr"><svg width="14" height="18" viewBox="0 0 14 18"><path d="M7 0a7 7 0 00-7 7c0 5 7 11 7 11s7-6 7-11a7 7 0 00-7-7zm0 9.5A2.5 2.5 0 117 4.5a2.5 2.5 0 010 5z" fill="#3fc1ea"/></svg><span>PO Box 410, Fairhaven,<br>NJ 08000, United States</span></div>
    <div>
      <div class="contact"><svg width="16" height="12" viewBox="0 0 16 12"><rect width="16" height="12" rx="2" fill="#3fc1ea"/><path d="M1 1l7 5 7-5" stroke="#141a3d" stroke-width="1.5" fill="none"/></svg><span>info@kestrelguard.com</span></div>
      <div class="contact" style="margin-top:8px"><svg width="16" height="16" viewBox="0 0 16 16"><circle cx="8" cy="8" r="8" fill="#3fc1ea"/></svg><span>kestrelguard.com</span></div>
    </div>
  </div>
</section>

<section class="card back">
  <div class="promo">
    <h2>PROTECTING YOUR<br>PEACE OF MIND</h2>
    <div class="rule"></div>
    <p>Our security guards are always one step ahead.</p>
    <div class="feature"><svg class="shield" viewBox="0 0 18 20"><path d="M9 0L18 3v6c0 6-4 9-9 11C4 18 0 15 0 9V3z" fill="#3fc1ea"/><path d="M5 10l3 3 5-6" stroke="#1b2350" stroke-width="2" fill="none"/></svg><span>HIGHLY TRAINED<br>PERSONEL</span></div>
    <div class="feature"><svg class="shield" viewBox="0 0 18 20"><path d="M9 0L18 3v6c0 6-4 9-9 11C4 18 0 15 0 9V3z" fill="#3fc1ea"/><path d="M5 10l3 3 5-6" stroke="#1b2350" stroke-width="2" fill="none"/></svg><span>RELIABLE SUPPORT<br>24 HOUR</span></div>
    <div class="web"><svg width="14" height="14" viewBox="0 0 16 16"><circle cx="8" cy="8" r="8" fill="#3fc1ea"/></svg>kestrelguard.com</div>
  </div>
  <div class="back-call"><span class="label">CALL NOW</span><svg width="16" height="16" viewBox="0 0 24 24"><path d="M6.6 10.8a15 15 0 006.6 6.6l2.2-2.2c.3-.3.7-.4 1-.2 1.1.4 2.3.6 3.6.6.6 0 1 .4 1 1V20c0 .6-.4 1-1 1A17 17 0 013 4c0-.6.4-1 1-1h3.5c.6 0 1 .4 1 1 0 1.3.2 2.5.6 3.6.1.3 0 .7-.2 1z" fill="#fff"/></svg><span class="num">555-014-2290</span></div>
  <div class="brand"><span class="brand-dot"></span>KESTREL</div>
</section>

</body>
</html>
```